Carwash Signage

We own and operate a 25m tunnel car wash in the uk. We are looking to upgrade our signage to include the following:-

Wash selection Board Size-1300x1300mm
Conditions 1300x1300mm
Instructions 1300x1300mm
Banner 2600x600mm
Stamp card flyer a5 double sided - 9 squares for stamping 3rd square needs to say free air freshener 9th square needs to say free vip car wash.

I have attached some notes for the details that are required to be included.

We are looking for a modern smart look more European car wash style than American car wash style. It should be bold and clear. with yellow/orange & blue/green,grey colours

The final design must be in a industry standard printable format.

UPDATED BRIEF AS DISCUSSED: We require design for 2 x window decals, flag design and 50% off voucher. Attached are rough layout drawings of what they should look like - we expect the designs to be in keeping with the previous designs colours, etc that have been carried out. We Look forward to hearing from you.

Target Market(s)

local car owners within a 15-20 mile radius

Colors
0054AA
0677BA
7BADD7
CADEEF
E8F1F8
0094D4
00A9DD
6FCCEA
C7EBF8
E9F6FB
00AB8E
00BBA5
67D7C9
C6EFE9
E9F9F6

Requirements
Must have
• must be sharp and modern European look

```html
<!DOCTYPE html>
<html lang="en">
<head>
<meta charset="utf-8">
<title>Pacifica Car Wash – Signage Set</title>
<link rel="stylesheet" href="https://fonts.googleapis.com/css2?family=Outfit:wght@400;500;600;700&family=Archivo+Black&family=Inter:wght@400&display=swap">
<style>
  :root {
    --sheet-grey: #b9b9b9;
    --label-ink: #111111;
    --board-top: #0a25c2;
    --board-mid: #1248cf;
    --board-bottom: #1d86d6;
    --band-cyan: #12a9e0;
    --cyan-text: #3fc6f2;
    --white: #ffffff;
    --tab-bg: #e8f1f8;
    --brand-navy: #0b2a9c;
    --teal: #00bba5;
    --teal-icon: #00ab8e;
    --check-green: #2ecf9a;
    --table-head: #c6efe9;
    --table-row: #ffffff;
    --table-row-alt: #e9f1f8;
    --table-line: #7badd7;
    --table-ink: #0b2a8a;
    --photo-light: #d6dde6;
    --photo-blue: #4a8fe0;
  }
  * { box-sizing: border-box; margin: 0; padding: 0; }
  html, body { width: 942px; height: 1200px; overflow: hidden; background: var(--sheet-grey); }
  body { position: relative; font-family: "Outfit", sans-serif; color: var(--white); }

  .sheet-label {
    position: absolute; font-family: "Inter", sans-serif; font-size: 14px;
    color: var(--label-ink); transform: translateX(-50%); white-space: nowrap;
  }

  .board {
    position: absolute; overflow: hidden;
    background: linear-gradient(180deg, var(--board-top) 0%, var(--board-mid) 45%, var(--board-bottom) 100%);
    box-shadow: 0 6px 18px rgba(0,0,0,0.18);
  }

  .brand-name {
    font-family: "Outfit", sans-serif; font-weight: 700; text-transform: uppercase;
    letter-spacing: 0.02em; white-space: nowrap; line-height: 1;
  }

  .brand-tab {
    position: absolute; top: 0; background: var(--tab-bg);
    border-radius: 0 0 10px 10px; display: flex; align-items: center; justify-content: center;
  }
  .brand-tab .brand-name { color: var(--brand-navy); }

  /* Banner */
  .banner { left: 48px; top: 46px; width: 844px; height: 195px;
    background: linear-gradient(100deg, #0a25c2 0%, #1450d4 60%, #1d70d8 100%); }
  .banner-offer { position: absolute; left: 65px; top: 13px; font-size: 22px; font-weight: 500;
    line-height: 1.1; color: var(--cyan-text); }
  .banner-brand { position: absolute; left: 365px; top: 30px; font-size: 24px; color: var(--white); }
  .banner-headline { position: absolute; left: 42px; top: 58px; font-family: "Archivo Black", sans-serif;
    font-size: 98px; line-height: 1; letter-spacing: -1px; color: var(--white); }
  .banner-band { position: absolute; left: 0; bottom: 0; width: 100%; height: 40px;
    background: linear-gradient(90deg, var(--band-cyan), #27b6e6); }
  .banner-band-text { position: absolute; left: 65px; top: 9px; font-size: 20px; font-weight: 600;
    letter-spacing: 0.28em; color: var(--white); white-space: nowrap; }
  .banner-photo { position: absolute; right: 0; top: 0; width: 258px; height: 195px;
    background: radial-gradient(ellipse at 55% 55%, var(--photo-light) 0%, #9fb4d6 45%, rgba(40,110,220,0.3) 80%, rgba(40,110,220,0) 100%); }

  /* Instructions */
  .instructions { left: 48px; top: 304px; width: 407px; height: 406px; }
  .instructions .brand-tab { left: 113px; width: 180px; height: 49px; }
  .instructions .brand-name { font-size: 17px; }
  .board-title { position: absolute; left: 0; width: 100%; top: 58px; text-align: center;
    font-size: 34px; font-weight: 700; letter-spacing: 0.01em; }
  .step-list { position: absolute; left: 22px; list-style: none; font-size: 12.2px; line-height: 16.6px; }
  .step-list li { position: relative; padding-left: 19px; width: 370px; }
  .step-list li svg { position: absolute; left: 0; top: 3px; width: 11px; height: 11px; }
  .steps-main { top: 100px; }
  .steps-end { top: 313px; }
  .check-list { position: absolute; left: 41px; top: 222px; list-style: none; font-size: 11.6px; line-height: 15.8px; }
  .check-list li { position: relative; padding-left: 18px; }
  .check-list li svg { position: absolute; left: 0; top: 3px; width: 10px; height: 10px; }
  .faint-photo { position: absolute; left: 120px; top: 200px; width: 287px; height: 206px;
    background: radial-gradient(ellipse at 55% 60%, rgba(190,210,240,0.22), rgba(190,210,240,0) 70%); }

  /* Wash selection */
  .selection { left: 486px; top: 304px; width: 407px; height: 406px; }
  .selection .brand-tab { left: 86px; width: 235px; height: 68px; }
  .selection .brand-name { font-size: 21px; }
  .disclaimer { position: absolute; left: 10px; width: 387px; top: 78px; text-align: center;
    font-size: 16.5px; font-weight: 500; line-height: 22.6px; }
  .risk-list { position: absolute; left: 31px; top: 153px; list-style: none; }
  .risk-list li { position: relative; width: 344px; height: 25px; margin-bottom: 3px;
    background: var(--teal); border-radius: 13px; padding-left: 41px;
    font-size: 16.5px; font-weight: 500; line-height: 25px; }
  .risk-list li svg { position: absolute; left: 19px; top: 6px; width: 13px; height: 13px; }
  .board-note { position: absolute; left: 20px; width: 367px; top: 356px; text-align: center;
    font-size: 8.6px; line-height: 13px; }

  /* Conditions */
  .conditions { left: 267px; top: 752px; width: 406px; height: 406px; }
  .conditions-brand { position: absolute; left: 0; width: 100%; top: 40px; text-align: center;
    font-size: 24px; color: var(--white); }
  .price-table { position: absolute; left: 14px; top: 94px; width: 379px; border-collapse: collapse;
    table-layout: fixed; color: var(--table-ink); font-weight: 600; text-align: center; }
  .price-table td, .price-table th { border: 0.6px solid var(--table-line); }
  .price-table thead th { background: var(--table-head); height: 45px; font-size: 5.4px; line-height: 7.4px; font-weight: 600; }
  .price-table tbody td { height: 45px; font-size: 8px; }
  .price-table tbody tr:nth-child(odd) td { background: var(--table-row); }
  .price-table tbody tr:nth-child(even) td { background: var(--table-row-alt); }
  .price-table .tier { font-size: 7.6px; line-height: 10px; }
  .price-table .price { font-size: 7.4px; }
  .price-table tfoot td { background: var(--table-head); height: 41px; font-size: 7.4px; line-height: 10px; }
  .slanted { display: inline-block; transform: rotate(-30deg); font-size: 6.4px; }
</style>
</head>
<body>

<svg width="0" height="0" style="position:absolute">
  <defs>
    <symbol id="sparkle" viewBox="0 0 20 20"><path d="M10 0 C11 7 13 9 20 10 C13 11 11 13 10 20 C9 13 7 11 0 10 C7 9 9 7 10 0Z"/></symbol>
    <symbol id="tick-dot" viewBox="0 0 20 20"><circle cx="10" cy="10" r="10"/><path d="M5.5 10.3 L8.7 13.3 L14.5 7" fill="none" stroke="#ffffff" stroke-width="2.4" stroke-linecap="round" stroke-linejoin="round"/></symbol>
  </defs>
</svg>

<!-- Banner -->
<div class="sheet-label" style="left:461px; top:22px;">Banner 2600 x 600 mm</div>
<section class="board banner">
  <div class="banner-photo" role="img" aria-label="Photo of a white SUV being splashed with water"></div>
  <p class="banner-offer">9x korting op een<br>schone auto!</p>
  <div class="brand-name banner-brand">Pacifica Car Wash</div>
  <h1 class="banner-headline">CAR WASH</h1>
  <div class="banner-band"><span class="banner-band-text">CASH + CARO PAYMENTS ACCEPTEO</span></div>
</section>

<!-- Instructions -->
<div class="sheet-label" style="left:257px; top:273px;">Instructions 1300 x 1300 mm</div>
<section class="board instructions">
  <div class="faint-photo" role="img" aria-label="Faint photo of a car in the wash tunnel"></div>
  <div class="brand-tab"><span class="brand-name">Pacifica Car Wash</span></div>
  <h2 class="board-title">INSTRUCTIONS</h2>
  <ul class="step-list steps-main">
    <li><svg fill="#00bba5"><use href="#sparkle"/></svg>Check for loose items before entering the wash</li>
    <li><svg fill="#00bba5"><use href="#sparkle"/></svg>Lower aerial if eletncal make sure the areal is fully retracted operator may assist but is not responsible for the condition of your car.</li>
    <li><svg fill="#00bba5"><use href="#sparkle"/></svg>Drive forward until operator tells you to stop.</li>
    <li><svg fill="#00bba5"><use href="#sparkle"/></svg>Operator will guide you into the car wash</li>
    <li><svg fill="#00bba5"><use href="#sparkle"/></svg>Once on conveyor track</li>
  </ul>
  <ul class="check-list">
    <li><svg fill="#2ecf9a"><use href="#tick-dot"/></svg>Hano Brace Off</li>
    <li><svg fill="#2ecf9a"><use href="#tick-dot"/></svg>Select Neutral Gear</li>
    <li><svg fill="#2ecf9a"><use href="#tick-dot"/></svg>Close all windows + sunroof</li>
    <li><svg fill="#2ecf9a"><use href="#tick-dot"/></svg>Leave engine running</li>
    <li><svg fill="#2ecf9a"><use href="#tick-dot"/></svg>Turn auto wipers off</li>
  </ul>
  <ul class="step-list steps-end">
    <li><svg fill="#00bba5"><use href="#sparkle"/></svg>Do not brace</li>
    <li><svg fill="#00bba5"><use href="#sparkle"/></svg>Do not steer</li>
    <li><svg fill="#00bba5"><use href="#sparkle"/></svg>Do not attempt exit vehicle</li>
    <li><svg fill="#00bba5"><use href="#sparkle"/></svg>At end of wash drive away when traffic light turns green</li>
  </ul>
</section>

<!-- Wash selection board -->
<div class="sheet-label" style="left:690px; top:273px;">Wash Selection Board -1300 x 1300 mm</div>
<section class="board selection">
  <div class="brand-tab"><span class="brand-name">Pacifica Car Wash</span></div>
  <p class="disclaimer">Pacifica car + commercials ltd cannot accept any responsibility for imliry, loss or damage callseo by the following:</p>
  <ul class="risk-list">
    <li><svg fill="#ffffff"><use href="#sparkle"/></svg>Non fully retractable aerials</li>
    <li><svg fill="#ffffff"><use href="#sparkle"/></svg>Roofs Racks</li>
    <li><svg fill="#ffffff"><use href="#sparkle"/></svg>Damaged Bodywork</li>
    <li><svg fill="#ffffff"><use href="#sparkle"/></svg>Loose trims</li>
    <li><svg fill="#ffffff"><use href="#sparkle"/></svg>Loose wing mirrors</li>
    <li><svg fill="#ffffff"><use href="#sparkle"/></svg>Loose exhalist systems</li>
    <li><svg fill="#ffffff"><use href="#sparkle"/></svg>Painted wheels</li>
  </ul>
  <p class="board-note">Remember the operator is here to help if in dolibt. Please ask for advice before entering the wash claims for damage cannot be entertained once vehicle has left site.</p>
</section>

<!-- Conditions / price board -->
<div class="sheet-label" style="left:471px; top:728px;">Conditions 1300 x 1300 mm</div>
<section class="board conditions">
  <div class="brand-name conditions-brand">Pacifica Car Wash</div>
  <table class="price-table">
    <colgroup>
      <col style="width:48px"><col style="width:44px"><col style="width:36px"><col style="width:31px">
      <col style="width:34px"><col style="width:32px"><col style="width:25px"><col style="width:34px">
      <col style="width:26px"><col style="width:34px"><col style="width:35px">
    </colgroup>
    <thead>
      <tr>
        <th><span class="slanted">OPTIONS</span></th>
        <th>ROOF BRUSH &amp; CONTOUR BRUSHES SILLBRUSHES</th>
        <th>DRYING DOUBLE CONTOLIR</th>
        <th>WAXING</th>
        <th>HAND BRUSH PREPARED</th>
        <th>ACTIVE FOAM PRESOAK</th>
        <th>JADE ULTRA WAS</th>
        <th>JET WASH PREWASH</th>
        <th>LINDER BODY WASH</th>
        <th>SNOW FOAM PREWASH</th>
        <th>PRICE</th>
      </tr>
    </thead>
    <tbody>
      <tr><td class="tier">VIP<br>PLATINUM</td><td>*</td><td>*</td><td>*</td><td>*</td><td>*</td><td>*</td><td>*</td><td>*</td><td>*</td><td class="price">€10.00</td></tr>
      <tr><td class="tier">GOLD</td><td>*</td><td>*</td><td>*</td><td>*</td><td>*</td><td>*</td><td>*</td><td></td><td></td><td class="price">€8.50</td></tr>
      <tr><td class="tier">SILVER</td><td>*</td><td>*</td><td>*</td><td>*</td><td>*</td><td></td><td></td><td></td><td></td><td class="price">€7.50</td></tr>
      <tr><td class="tier">BRONZE</td><td>*</td><td>*</td><td>*</td><td>*</td><td></td><td></td><td></td><td></td><td></td><td class="price">€6.50</td></tr>
    </tbody>
    <tfoot>
      <tr>
        <td><span class="slanted">OFFERS</span></td>
        <td colspan="4">VIP PLATINUM WASH PACK<br>BUY 2 GET 1F REE<br>€20.00</td>
        <td colspan="6">LOYALTY CARD AVAILABLE<br>WASH + EARN<br>ASK THE OPERATOR FOR DETAILS</td>
      </tr>
    </tfoot>
  </table>
</section>

</body>
</html>
```